Business Cards for GPS Technology Business - Logo Supplied

Brelka Technologies Ltd. requires a business card design. Brelka is a startup GPS vehicle fleet tracking vendor. Our hardware/software helps business fleets be more productive and reduce operating costs. Our systems utilize a mix of GPS satellite, cell network and web technologies.
We would like to see a double sided original design utilizing our existing logo. Please use whatever colors will work with the blue logo.
As a business, we want to project the image of friendly and approachable lifetime business partners and advisors to our customers - “someone you can trust”. Words customers will use to describe us will include: knowledgeable, supportive, trustworthy and honest.
We will also require Viewtube, Chirpnet, Pagebook and Lookup+ backgrounds. Winner will be first in line to quote for this work (separate project).
Updates
Hello designers!
Target Market(s)
Target audience are working owners and managers of vehicle fleets. Usually male, age 30 to 60. Often have a trades background.
Industry/Entity Type
Business
Font styles to use
Requirements
Must have
- Please use the following dummy data for the design:
name: Ned Brelka
title: Director
address: 2389 Marlow Drive
city: Kelvaton, BC
postal code: K7P 2T4
cell phone number: 555-214-7730
business number: 555-309-4412
toll free number: 1-800-555-0199
web site address: www.brelka-example.com
tagline: GPS Fleet Tracking Specialists
Nice to have
- Abstract imagery relating to GPS tracking / fleet vehicles / technology
Should not have
- Do not use serif fonts.

```html
<!DOCTYPE html>
<html lang="en">
<head>
<meta charset="utf-8">
<title>Brelka Technologies – Business Card</title>
<link href="https://fonts.googleapis.com/css2?family=Mulish:wght@400;700;800&display=swap" rel="stylesheet">
<style>
  :root {
    --stage: #1a1a1c;
    --brand-blue: #1e63ad;
    --brand-blue-deep: #0f4a8c;
    --brand-blue-light: #3a86d0;
    --ghost-blue: #e8eff7;
    --ink: #2b2b2b;
    --rule: #8a8a8a;
    --paper: #ffffff;
  }
  * { box-sizing: border-box; margin: 0; padding: 0; }
  html, body { width: 1200px; height: 871px; overflow: hidden; }
  body {
    background: var(--stage);
    font-family: "Mulish", Arial, sans-serif;
    position: relative;
  }
  .card {
    position: absolute;
    width: 560px;
    height: 320px;
    overflow: hidden;
    border-radius: 2px;
    box-shadow: 0 18px 40px rgba(0,0,0,.55);
  }

  /* Front side */
  .card-front {
    left: 90px; top: 100px;
    background: linear-gradient(160deg, var(--brand-blue-light) 0%, var(--brand-blue) 50%, var(--brand-blue-deep) 100%);
  }
  .card-front .ghost-name {
    position: absolute; left: 10px; top: 60px;
    font-weight: 800; font-size: 190px; line-height: 1;
    color: rgba(255,255,255,.10); letter-spacing: -4px;
    white-space: nowrap;
  }
  .card-front .wordmark {
    position: absolute; left: 0; right: 0; top: 112px;
    text-align: center;
    font-weight: 800; font-size: 76px; line-height: 1;
    color: var(--paper); letter-spacing: -1px;
  }
  .card-front .web {
    position: absolute; left: 0; right: 0; top: 202px;
    text-align: center;
    font-weight: 700; font-size: 15px; letter-spacing: 1px;
    color: rgba(255,255,255,.9);
  }

  /* Back side */
  .card-back {
    left: 550px; top: 450px;
    background: var(--paper);
  }
  .card-back .ghost-name {
    position: absolute; left: 250px; top: -20px;
    font-weight: 800; font-size: 200px; line-height: 1;
    color: var(--ghost-blue); letter-spacing: -4px;
    white-space: nowrap;
  }
  .card-back .wordmark {
    position: absolute; left: 36px; top: 24px;
    font-weight: 800; font-size: 66px; line-height: 1;
    color: var(--brand-blue); letter-spacing: -1px;
  }
  .contact-list {
    position: absolute; left: 28px; top: 128px;
    list-style: none;
    font-size: 13px; line-height: 20px; color: var(--ink);
  }
  .contact-list li { display: flex; align-items: center; gap: 14px; }
  .contact-list svg { width: 11px; height: 11px; fill: var(--brand-blue); flex: none; }
  .person {
    position: absolute; right: 40px; top: 168px;
    text-align: right;
  }
  .person .name {
    font-weight: 700; font-size: 20px; color: var(--brand-blue);
    padding-bottom: 2px;
  }
  .person .role {
    font-size: 15px; color: var(--ink);
    border-top: 1px solid var(--rule);
    padding-top: 1px; width: 250px; margin-left: auto;
  }
  .address {
    position: absolute; right: 40px; top: 228px;
    text-align: right; font-size: 13.5px; line-height: 20px; color: var(--ink);
    font-style: normal;
  }
  .tagline-band {
    position: absolute; left: 0; right: 0; bottom: 0; height: 34px;
    background: linear-gradient(90deg, var(--brand-blue) 0%, var(--brand-blue-deep) 100%);
    display: flex; align-items: center; padding-left: 28px;
  }
  .tagline-band p {
    font-weight: 700; font-size: 13px; letter-spacing: 4px;
    text-transform: uppercase; color: var(--paper);
  }
  .band-lead {
    position: absolute; left: 0; bottom: 34px; width: 300px; height: 6px;
    background: var(--brand-blue);
  }
</style>
</head>
<body>

  <section class="card card-front" aria-label="Business card front">
    <div class="ghost-name" aria-hidden="true">Brelka</div>
    <div class="wordmark">Brelka</div>
    <div class="web">www.brelka-example.com</div>
  </section>

  <section class="card card-back" aria-label="Business card back">
    <div class="ghost-name" aria-hidden="true">Brelka</div>
    <div class="wordmark">Brelka</div>

    <ul class="contact-list">
      <li><svg viewBox="0 0 12 12" aria-hidden="true"><path d="M2 1h2l1 3-1.5 1a7 7 0 0 0 3.5 3.5L8 7l3 1v2a1 1 0 0 1-1 1A9 9 0 0 1 1 2a1 1 0 0 1 1-1z"/></svg>1-800-555-0199 Toll Free</li>
      <li><svg viewBox="0 0 12 12" aria-hidden="true"><path d="M2 1h2l1 3-1.5 1a7 7 0 0 0 3.5 3.5L8 7l3 1v2a1 1 0 0 1-1 1A9 9 0 0 1 1 2a1 1 0 0 1 1-1z"/></svg>555-309-4412</li>
      <li><svg viewBox="0 0 12 12" aria-hidden="true"><rect x="3" y="0.5" width="6" height="11" rx="1"/></svg>555-214-7730</li>
      <li><svg viewBox="0 0 12 12" aria-hidden="true"><path d="M0.5 2.5h11v7h-11zM1 3l5 4 5-4" stroke="#fff" stroke-width=".8"/></svg>ned@brelka-example.com</li>
      <li><svg viewBox="0 0 12 12" aria-hidden="true"><circle cx="6" cy="6" r="5.5"/></svg>www.brelka-example.com</li>
    </ul>

    <div class="person">
      <p class="name">Ned Brelka</p>
      <p class="role">Director</p>
    </div>

    <address class="address">
      2389 Marlow Drive<br>
      Kelvaton, BC K7P 2T4
    </address>

    <div class="band-lead" aria-hidden="true"></div>
    <div class="tagline-band"><p>GPS Fleet Tracking Specialists</p></div>
  </section>

</body>
</html>
```